4R Capital business cards for a tech VC

We're starting a new Venture Capital that is focusing on bringing the best start ups from Israel to NYC
We need a business cards template for this that gives the sense of an entrepreneurial look
I don't want any religious signs on this even thought it's Israel
I'm looking for a techi feeling but not too crazy
The card should probably be in the same light blue as the logo and the logo in white

Target Market(s)

Investors

Industry/Entity Type

Tech

Contact Information for Business Card

The card needs to look slick and entrepreneurship like
The VC is focused on NYC and Tel Aviv so could be great to show something on the back side that is like NYC skyline or something like that
You can see the logo attached

Colors
0455a3
3276b5
85acd3
cedeed
eaf1f7

Requirements
Must have
• A very cool looking business card that shows we're a cutting edge tech VC with a focus on bringing start ups from Tel Aviv and leveraging the NYC ecosystem
Nice to have
• NYC skyline can be cool , maybe something that is connected to Tel Aviv

```html
<!DOCTYPE html>
<html lang="en">
<head>
<meta charset="utf-8">
<title>4R Capital – Business Card</title>
<link rel="stylesheet" href="https://fonts.googleapis.com/css2?family=Roboto:wght@300;400;500;700&display=swap">
<style>
  :root {
    --bg: #e4e4e4;
    --paper: #ffffff;
    --brand: #1e88cf;
    --brand-deep: #0455a3;
    --back-light: #1a86c4;
    --back-dark: #0b5485;
    --ink: #4a4a4a;
    --rule: #3a93d3;
  }
  * { box-sizing: border-box; margin: 0; padding: 0; }
  html, body { width: 1200px; height: 1200px; overflow: hidden; }
  body {
    background: var(--bg);
    font-family: "Roboto", Arial, sans-serif;
    position: relative;
  }
  .card {
    position: absolute;
    top: 440px;
    width: 540px;
    height: 310px;
    border-radius: 3px;
    box-shadow: 0 6px 18px rgba(0,0,0,0.18);
    overflow: hidden;
  }
  .card--front { left: 40px; background: var(--paper); }
  .card--back {
    left: 620px;
    background: radial-gradient(ellipse at 55% 45%, var(--back-light) 0%, #136fa8 50%, var(--back-dark) 100%);
    display: flex;
    align-items: center;
    justify-content: center;
  }
  .wordmark {
    position: absolute;
    left: 34px;
    top: 30px;
    font-size: 40px;
    font-weight: 700;
    color: var(--brand);
    letter-spacing: 1px;
  }
  .card--back .wordmark {
    position: static;
    font-size: 64px;
    color: var(--brand-deep);
  }
  .divider {
    position: absolute;
    left: 40px;
    right: 40px;
    top: 108px;
    height: 1px;
    background: var(--rule);
  }
  .address {
    position: absolute;
    left: 40px;
    top: 124px;
    font-size: 13px;
    line-height: 20px;
    color: var(--ink);
  }
  .address svg { width: 11px; height: 11px; vertical-align: -1px; margin-right: 4px; fill: var(--brand); }
  .person {
    position: absolute;
    right: 40px;
    top: 180px;
    text-align: right;
  }
  .person__name { font-size: 24px; font-weight: 300; color: var(--brand); letter-spacing: 0.5px; }
  .person__role { font-size: 13px; color: var(--ink); margin-top: 2px; }
  .person__rule { height: 1px; background: var(--rule); width: 190px; margin: 8px 0 8px auto; }
  .contacts { list-style: none; font-size: 13px; line-height: 20px; color: var(--ink); }
  .contacts svg { width: 12px; height: 12px; vertical-align: -2px; margin-left: 6px; fill: var(--brand); }
</style>
</head>
<body>
  <section class="card card--front" aria-label="Business card front">
    <div class="wordmark">4R Capital</div>
    <div class="divider"></div>
    <div class="address">
      <div><svg viewBox="0 0 12 12"><path d="M6 1 L11 6 H9.5 V11 H7 V8 H5 V11 H2.5 V6 H1 Z"/></svg>Dummy city</div>
      <div>Dummy Country Land</div>
    </div>
    <div class="person">
      <div class="person__name">DANA LEVI</div>
      <div class="person__role">Director</div>
      <div class="person__rule"></div>
      <ul class="contacts">
        <li>1-555-014-2290<svg viewBox="0 0 12 12"><path d="M2 4 Q6 0 10 4 L9 6 L7.5 5 V4 H4.5 V5 L3 6 Z M3 7 H9 V11 H3 Z"/></svg></li>
        <li>www.4rcapital.com<svg viewBox="0 0 12 12"><circle cx="6" cy="6" r="5.5"/></svg></li>
        <li>dana@4rcapital.com<svg viewBox="0 0 12 12"><path d="M1 2.5 H11 V9.5 H1 Z"/></svg></li>
      </ul>
    </div>
  </section>
  <section class="card card--back" aria-label="Business card back">
    <div class="wordmark">4R Capital</div>
  </section>
</body>
</html>
```